We Buy Houses Website

Looking for a highly motivated and skillfull designer to design and code me a "we Buy Houses" type website. I have a potential logo, but if you think you can make a BETTER one, please do try and incorporate it in your template. I am looking for creativity, professionalism, simple yet elegant. I will need a simple form on the front of the template along with pictures I provide you of recent houses I have bought. Look at these sites for examples of the layout of the website:

http://www.brickvalehomes.example/
http://www.petrafixeshouses.example/
http://www.quickpropertyexitnow.example/

If you make me a design that blows me away, and you are dependable, you will become part of my team and in charge of the web aspect which will include designing, updating, any and all graphics and logo work, SEO, coding. If you have skills in all of these areas please make me a design and lets do business!! The name of the website will be "Lurt Takes Homes" at LurtTakesHomes.example

I have uploaded some pictures of houses that we have done, please feel free to incorporate this into the banner or the design, etc. I want them to know we buy houses in ANY condition, as is, cash, can close immediately so they can get on with their life. We have many options to help them find a solution to whatever problem they have. We are in the business of helping people.

Target Market(s)

People looking to sell their houses
people facing foreclosure, bankruptcy, death in the family, divorce, anyone that we can help
people with ugly houses that need a lot of repair

Industry/Entity Type

Business

Font styles to use
Serif
Sans Serif

Colors

Designer to choose colors to be used in the design.

Requirements
Must have
• must have a simple form on the front of the page, preferrably near the banner, with the few required fields to help someone get started putting in their interest to sell their house, view the 2 websites i put as examples to see what kind of fields it should have.

My phone number (555) 482-1937 along with a Lurt Takes Homes logo, clean simple and elegant and professional. I want a nice color scheme that is not white but professional and has a wow factor.

```html
<!DOCTYPE html>
<html lang="en">
<head>
<meta charset="utf-8">
<title>Lurt Takes Homes — We Buy Houses</title>
<link rel="stylesheet" href="https://fonts.googleapis.com/css2?family=Roboto+Condensed:wght@400;700&family=Arimo:wght@400;700&display=swap">
<style>
:root{
  --ink:#0a0e28;
  --nav:#141a38;
  --deep:#0e1747;
  --band:#1e295a;
  --foot:#0b1136;
  --lime:#b5e61d;
  --lime-dark:#6da514;
  --white:#ffffff;
  --muted:#c5c9d8;
  --btn:#55575f;
  --line:#27306a;
}
*{margin:0;padding:0;box-sizing:border-box}
html,body{width:968px;height:1200px;overflow:hidden;background:var(--deep)}
body{position:relative;font-family:"Arimo",Arial,sans-serif;color:var(--white)}
.abs{position:absolute}

/* header */
.site-header{left:0;top:0;width:968px;height:78px;background:var(--ink)}
.brand{left:139px;top:42px;display:flex;align-items:center;gap:7px}
.brand-mark{width:12px;height:12px;background:var(--lime)}
.brand-name{font-family:"Roboto Condensed",sans-serif;font-weight:700;font-size:17px;color:var(--lime);letter-spacing:.3px}
.call{left:629px;top:27px;display:flex;align-items:center;gap:7px;font-family:"Roboto Condensed",sans-serif;font-size:18px;font-weight:400;white-space:nowrap}
.call-icon{width:24px;height:24px;border-radius:5px;background:#56b8e6;display:flex;align-items:center;justify-content:center}
.call b{font-weight:400;color:var(--lime)}

/* nav */
.main-nav{left:0;top:78px;width:968px;height:33px;background:var(--nav)}
.main-nav a{position:absolute;top:11px;font-family:"Roboto Condensed",sans-serif;font-weight:700;font-size:9.5px;color:var(--white);text-decoration:none;white-space:nowrap}

/* hero */
.hero{left:0;top:111px;width:968px;height:359px;
  background:
    radial-gradient(ellipse 140px 180px at 40px 220px, rgba(70,110,40,.95), rgba(70,110,40,0)),
    radial-gradient(ellipse 120px 120px at 120px 250px, rgba(196,150,200,.55), rgba(196,150,200,0)),
    radial-gradient(ellipse 110px 90px at 330px 340px, rgba(110,150,200,.7), rgba(110,150,200,0)),
    radial-gradient(ellipse 170px 190px at 560px 190px, rgba(244,236,222,.95), rgba(244,236,222,0)),
    radial-gradient(ellipse 120px 140px at 680px 120px, rgba(200,160,130,.55), rgba(200,160,130,0)),
    radial-gradient(ellipse 130px 110px at 740px 300px, rgba(165,210,230,.85), rgba(165,210,230,0)),
    radial-gradient(ellipse 120px 160px at 880px 120px, rgba(245,245,245,.8), rgba(245,245,245,0)),
    radial-gradient(ellipse 140px 80px at 860px 330px, rgba(110,80,60,.55), rgba(110,80,60,0)),
    linear-gradient(90deg,#56703a 0%,#8e9a80 14%,#bfc6c6 32%,#d9dcdf 55%,#b7c2cc 80%,#8f9fae 100%)}
.hero-arrow{width:36px;height:36px;border-radius:50%;border:2px solid rgba(255,255,255,.45);top:277px}
.lead-form{left:156px;top:131px;width:233px;height:320px;background:rgba(255,255,255,.86)}
.lead-form h1{position:absolute;left:0;top:22px;width:100%;text-align:center;font-family:"Roboto Condensed",sans-serif;font-weight:700;font-size:23px;line-height:24px;color:#0d1130}
.field{position:absolute;left:18px;width:198px;height:22px;background:#fff;border:1px solid #b9bcc4;font-size:6.5px;color:#777;padding:7px 0 0 9px}
.submit{position:absolute;left:18px;top:273px;width:198px;height:28px;background:linear-gradient(#9ed432,var(--lime-dark));color:#fff;font-family:"Arimo",sans-serif;font-weight:700;font-size:12px;text-align:center;line-height:28px}
.badge{left:716px;top:167px;width:156px;height:156px;border-radius:50%;background:var(--ink);text-align:center}
.badge .brand-name{display:block;margin-top:70px;font-size:11.5px;font-weight:400}
.badge .hrs{display:block;margin-top:6px;font-family:"Roboto Condensed",sans-serif;font-size:17px;color:var(--lime);line-height:17px}
.badge .svc{display:block;font-family:"Roboto Condensed",sans-serif;font-size:13px;font-weight:700;color:#fff}

/* columns */
.col-title{font-family:"Roboto Condensed",sans-serif;font-weight:700;font-size:14.5px;line-height:18px;top:504px}
.col-title span{color:var(--lime);display:block}
.about-photo{left:139px;top:547px;width:234px;height:103px;background:linear-gradient(120deg,#8fb2d8,#dfe4ea 50%,#8a7a6a)}
.about-text{left:139px;top:657px;width:240px;font-size:8.4px;line-height:16px;color:var(--muted)}
.more-btn{width:66px;height:19px;background:var(--btn);border-radius:2px;font-size:7px;color:#e6e6e6;text-align:center;line-height:19px;top:768px}
.item{width:190px;height:70px;border-bottom:1px solid var(--line)}
.item .thumb{position:absolute;left:0;top:0;width:56px;height:49px;border:2px solid #2d3566}
.item h3{position:absolute;left:68px;top:0;font-size:8.6px;font-weight:400;white-space:nowrap}
.item p{position:absolute;left:68px;top:14px;width:128px;font-size:7.3px;line-height:12px;color:var(--muted)}
.item a{position:absolute;left:68px;top:41px;font-size:6.6px;color:var(--lime);text-decoration:none}

/* featured */
.featured{left:0;top:826px;width:968px;height:289px;background:var(--band)}
.feat-title{left:139px;top:856px;font-family:"Roboto Condensed",sans-serif;font-weight:700;font-size:14.5px}
.feat-title span{color:var(--lime)}
.pager{top:858px;width:19px;height:19px;background:#2f3a6a}
.prop{top:892px;width:173px;height:152px}
.prop-cap{top:1058px;width:173px;text-align:center;font-family:"Roboto Condensed",sans-serif;font-size:9px;color:var(--lime)}
.prop-link{top:1076px;width:173px;text-align:center;font-size:7.5px;color:#fff}

/* footer */
.site-footer{left:0;top:1115px;width:968px;height:85px;background:var(--foot)}
.foot-nav a{position:absolute;top:1142px;font-family:"Roboto Condensed",sans-serif;font-weight:700;font-size:8px;color:#c9ccd8;text-decoration:none;white-space:nowrap}
.copyright{left:139px;top:1164px;font-family:"Roboto Condensed",sans-serif;font-weight:700;font-size:8px;color:#c9ccd8}
.social{top:1147px;width:25px;height:25px;border-radius:50%;border:1.5px solid #8e93ad;display:flex;align-items:center;justify-content:center}
.social svg{display:block}
</style>
</head>
<body>

<header class="abs site-header">
  <div class="abs brand"><span class="brand-mark"></span><span class="brand-name">LURT TAKES HOMES</span></div>
  <div class="abs call">
    <span class="call-icon"><svg width="14" height="14" viewBox="0 0 24 24"><path fill="#fff" d="M6.6 10.8a15 15 0 0 0 6.6 6.6l2.2-2.2c.3-.3.7-.4 1-.2 1.1.4 2.3.6 3.6.6.6 0 1 .4 1 1V20c0 .6-.4 1-1 1A17 17 0 0 1 3 4c0-.6.4-1 1-1h3.5c.6 0 1 .4 1 1 0 1.3.2 2.5.6 3.6.1.3 0 .7-.2 1z"/></svg></span>
    <span>CALL US : <b>(555) 482-1937</b></span>
  </div>
</header>

<nav class="abs main-nav">
  <a style="left:157px">ABOUT</a>
  <a style="left:212px">BUY A HOUSE</a>
  <a style="left:293px">SELL A HOUSE</a>
  <a style="left:377px">RENT A HOUSE</a>
  <a style="left:462px">INVESTORS</a>
  <a style="left:535px">FRANCHISE INFO</a>
  <a style="left:627px">FAQS TESTIMONIALS</a>
  <a style="left:734px">HOW DOES IT WORK?</a>
</nav>

<section class="abs hero" role="img" aria-label="Smiling family of four sitting outdoors in front of their home with a garden"></section>
<div class="abs hero-arrow" style="left:36px"></div>
<div class="abs hero-arrow" style="left:879px">
  <svg width="32" height="32" viewBox="0 0 32 32"><path d="M12 9l9 7-9 7z" fill="rgba(255,255,255,.5)"/></svg>
</div>

<form class="abs lead-form">
  <h1>WE'LL BUY<br>YOUR HOUSE!</h1>
  <div class="field" style="top:80px">NAME :</div>
  <div class="field" style="top:112px">EMAIL :</div>
  <div class="field" style="top:144px">PHONE :</div>
  <div class="field" style="top:176px">PROPERTY ADDRESS :</div>
  <div class="field" style="top:208px;width:94px">ALABAMA</div>
  <div class="field" style="top:208px;left:122px;width:94px">CITY :</div>
  <div class="field" style="top:241px">ZIP CODE :</div>
  <div class="submit">SUBMIT NOW</div>
</form>

<div class="abs badge">
  <span class="brand-name">LURT TAKES HOMES</span>
  <span class="hrs">24 HOURS</span>
  <span class="svc">SERVICES</span>
</div>

<!-- about -->
<h2 class="abs col-title" style="left:139px">ABOUT<span>LURT TAKES HOMES</span></h2>
<div class="abs about-photo" role="img" aria-label="Hand holding a small model house"></div>
<p class="abs about-text">Lorem Ipsum is simply dummy text of the printing and typesetting industry. Lorem Ipsum has been the industry's standard dummy text ever since the 1500s, when an unknown printer took a galley of type and scrambled it to make a type specimen book. It has survived not only five centuries, but also the leap into electronic typesetting...</p>
<div class="abs more-btn" style="left:139px">READ MORE</div>

<!-- recent -->
<h2 class="abs col-title" style="left:406px">RECENT<span>UPDATES FOR SALE</span></h2>
<div class="abs item" style="left:407px;top:550px"><div class="thumb" role="img" aria-label="Bedroom interior" style="background:linear-gradient(#6b4a36,#d9c2a6)"></div><h3>LOREM IPSUM IS SIMPLY</h3><p>Lorem Ipsum is simply dummy text of the printing typesetting industry.</p><a>[ VIEW MORE ]</a></div>
<div class="abs item" style="left:407px;top:626px"><div class="thumb" role="img" aria-label="House exterior at dusk" style="background:linear-gradient(#24407a,#c07a3a)"></div><h3>LOREM IPSUM IS SIMPLY</h3><p>Lorem Ipsum is simply dummy text of the printing typesetting industry.</p><a>[ VIEW MORE ]</a></div>
<div class="abs item" style="left:407px;top:701px;border:0"><div class="thumb" role="img" aria-label="House with green lawn" style="background:linear-gradient(#7ea4d6,#d8d2c4 55%,#4f8a2c)"></div><h3>LOREM IPSUM IS SIMPLY</h3><p>Lorem Ipsum is simply dummy text of the printing typesetting industry.</p><a>[ VIEW MORE ]</a></div>
<div class="abs more-btn" style="left:407px">READ MORE</div>

<!-- stories -->
<h2 class="abs col-title" style="left:634px">SUCCESSFULL<span>STORIES</span></h2>
<div class="abs item" style="left:634px;top:550px"><div class="thumb" role="img" aria-label="Villa with pool at night" style="background:linear-gradient(#2a3f80,#c98a4a 60%,#3aa2d8)"></div><h3>LOREM IPSUM IS SIMPLY</h3><p>Lorem Ipsum is simply dummy text of the printing typesetting industry.</p><a>[ VIEW MORE ]</a></div>
<div class="abs item" style="left:634px;top:626px"><div class="thumb" role="img" aria-label="Stone mansion exterior" style="background:linear-gradient(#8aa6c8,#b9a88e 55%,#5a6a3a)"></div><h3>LOREM IPSUM IS SIMPLY</h3><p>Lorem Ipsum is simply dummy text of the printing typesetting industry.</p><a>[ VIEW MORE ]</a></div>
<div class="abs item" style="left:634px;top:701px;border:0"><div class="thumb" role="img" aria-label="Modern house with pool" style="background:linear-gradient(#3f6fb8,#e0d8cc 50%,#2aa0d6)"></div><h3>LOREM IPSUM IS SIMPLY</h3><p>Lorem Ipsum is simply dummy text of the printing typesetting industry.</p><a>[ VIEW MORE ]</a></div>
<div class="abs more-btn" style="left:634px">READ MORE</div>

<!-- featured -->
<section class="abs featured"></section>
<h2 class="abs feat-title">FEATURED <span>PROPERTIES</span></h2>
<div class="abs pager" style="left:789px"><svg width="19" height="19"><path d="M11 5l-4 4.5 4 4.5" stroke="#9aa0c0" fill="none"/></svg></div>
<div class="abs pager" style="left:809px"><svg width="19" height="19"><path d="M8 5l4 4.5-4 4.5" stroke="#9aa0c0" fill="none"/></svg></div>

<div class="abs prop" style="left:139px;background:linear-gradient(#2e2a26,#6a4a30 60%,#3a342e)" role="img" aria-label="Kitchen with wooden cabinets"></div>
<div class="abs" style="left:212px;top:956px;width:25px;height:25px;border-radius:50%;background:rgba(255,255,255,.75)">
  <svg width="25" height="25" viewBox="0 0 25 25"><g stroke="#555" stroke-width="2" fill="none"><rect x="7" y="11" width="7" height="4" rx="2" transform="rotate(-45 10.5 13)"/><rect x="11" y="9" width="7" height="4" rx="2" transform="rotate(-45 14.5 11)"/></g></svg>
</div>
<div class="abs prop" style="left:312px;background:linear-gradient(#3a3a44,#8a6a4a 50%,#1e1e22)" role="img" aria-label="Bathroom with vanity and toilet"></div>
<div class="abs prop" style="left:485px;background:linear-gradient(#6a4028,#b88a5a 55%,#d8c4a8)" role="img" aria-label="Kitchen with tiled floor"></div>
<div class="abs prop" style="left:658px;background:linear-gradient(#a08a6a,#e8e4dc 50%,#9a8878)" role="img" aria-label="Bright living room"></div>

<div class="abs prop-cap" style="left:139px">LOREM IPSUM IS SIMPLY DUMMY</div>
<div class="abs prop-cap" style="left:312px">LOREM IPSUM IS SIMPLY DUMMY</div>
<div class="abs prop-cap" style="left:485px">LOREM IPSUM IS SIMPLY DUMMY</div>
<div class="abs prop-cap" style="left:658px">LOREM IPSUM IS SIMPLY DUMMY</div>
<div class="abs prop-link" style="left:139px">[ VIEW THE DETAILS ]</div>
<div class="abs prop-link" style="left:312px">[ VIEW THE DETAILS ]</div>
<div class="abs prop-link" style="left:485px">[ VIEW THE DETAILS ]</div>
<div class="abs prop-link" style="left:658px">[ VIEW THE DETAILS ]</div>

<!-- footer -->
<footer class="abs site-footer"></footer>
<nav class="foot-nav">
  <a style="left:139px">ABOUT</a>
  <a style="left:183px">BUY A HOUSE</a>
  <a style="left:248px">SELL A HOUSE</a>
  <a style="left:316px">RENT A HOUSE</a>
  <a style="left:385px">INVESTORS</a>
  <a style="left:443px">FRANCHISE INFO</a>
  <a style="left:518px">FAQS TESTIMONIALS</a>
  <a style="left:606px">HOW DOES IT WORK?</a>
</nav>
<div class="abs copyright">COPYRIGHT © 2014 LURT TAKES HOMES. ALL RIGHTS RESERVED.</div>

<!-- generic contact icons: share, chat, mail, globe -->
<div class="abs social" style="left:717px" aria-label="Share">
  <svg width="12" height="12" viewBox="0 0 12 12"><g fill="#c9ccd8"><circle cx="9.5" cy="2.5" r="1.7"/><circle cx="2.5" cy="6" r="1.7"/><circle cx="9.5" cy="9.5" r="1.7"/></g><path d="M9.5 2.5L2.5 6l7 3.5" stroke="#c9ccd8" stroke-width="1" fill="none"/></svg>
</div>
<div class="abs social" style="left:746px" aria-label="Chat">
  <svg width="12" height="12" viewBox="0 0 12 12"><path d="M1.5 2h9v6h-5l-2.5 2.2V8h-1.5z" fill="none" stroke="#c9ccd8" stroke-width="1.1" stroke-linejoin="round"/></svg>
</div>
<div class="abs social" style="left:775px" aria-label="Email">
  <svg width="12" height="12" viewBox="0 0 12 12"><rect x="1" y="2.5" width="10" height="7" fill="none" stroke="#c9ccd8" stroke-width="1.1"/><path d="M1 2.5l5 4 5-4" fill="none" stroke="#c9ccd8" stroke-width="1.1"/></svg>
</div>
<div class="abs social" style="left:804px" aria-label="Website">
  <svg width="12" height="12" viewBox="0 0 12 12"><g fill="none" stroke="#c9ccd8" stroke-width="1"><circle cx="6" cy="6" r="4.8"/><ellipse cx="6" cy="6" rx="2" ry="4.8"/><path d="M1.2 6h9.6"/></g></svg>
</div>

</body>
</html>
```